Crust Harbor wants to rebrand thier Menu/Image

Looking to re brand to a more casual hip vibe. I was thinking a simple "sketch feel" Kraft Paper Menu. I have uploaded some inspirational images. The menu will serve as a jumping off point to re brand our web presence. (www.crustharbor.org). and eventually our decor. Take a look at our web page for a feel of what we do and who we are

Target Market(s)

Pizza Take Out Quick Serve Customers. Family Restaurant

Requirements
Must have
• -Adaptable to become in house menu.
• - Use our existing logo
• -playful, fun, hip not to sophisticated
• --Use "Traditional Quality Control Image". (three guys)
• Cool (tone) Kraft Paper. Black/Sepia text. Touches of "Pizza Sauce" red

```html
<!DOCTYPE html>
<html lang="en">
<head>
<meta charset="utf-8">
<title>Crust Harbor Menu</title>
<link href="https://fonts.googleapis.com/css2?family=Alfa+Slab+One&family=Oswald:wght@400;500;600&family=Roboto+Condensed:wght@400;700&family=Yellowtail&family=Rye&family=Special+Elite&family=Bebas+Neue&family=Playfair+Display:wght@700&display=swap" rel="stylesheet">
<style>
:root{
  --kraft:#ccb08b;
  --kraft-dark:#b99a74;
  --ink:#2b2420;
  --sepia:#4a3d33;
  --sauce:#b3262b;
  --rule:#5a4a3c;
}
*{margin:0;padding:0;box-sizing:border-box}
html,body{width:798px;height:1200px;overflow:hidden;background:var(--kraft)}
.menu{position:relative;width:798px;height:1200px;background:radial-gradient(ellipse at 50% 40%,#d3b793 0%,var(--kraft) 60%,var(--kraft-dark) 100%);color:var(--ink);font-family:'Roboto Condensed',sans-serif;overflow:hidden}
.abs{position:absolute}
.art{position:absolute;border-radius:40%;opacity:.45}
.rule-v{position:absolute;left:399px;top:14px;width:1px;height:1172px;background:var(--rule);opacity:.6}
.rule-h{position:absolute;left:410px;width:374px;height:1px;background:var(--rule);opacity:.6}
.slab{font-family:'Alfa Slab One',serif;color:var(--sauce);letter-spacing:1px}
.script{font-family:'Yellowtail',cursive;color:var(--sauce)}
.item{font-family:'Oswald',sans-serif;font-weight:600;font-size:12.5px;line-height:1.05;text-transform:uppercase;color:var(--ink)}
.item .p{font-size:9px}
.desc{font-family:'Roboto Condensed',sans-serif;font-size:6.4px;line-height:1.2;text-transform:uppercase;color:var(--sepia);margin-bottom:6px}
.sal{font-family:'Special Elite',cursive;font-size:14px;line-height:1.05;color:var(--ink)}
.sal .p{font-size:9px}
.col{position:absolute}
.sub{font-family:'Oswald',sans-serif;font-size:9px;color:var(--sauce);text-transform:uppercase;text-align:center}
.pz{position:absolute;width:190px;text-align:center}
.pz .n{color:var(--ink);line-height:1}
.pz .d{font-size:6.2px;text-transform:uppercase;color:var(--sepia);line-height:1.25;margin-top:3px}
.sig-title{position:absolute;left:414px;top:16px;width:196px;text-align:center;white-space:nowrap;overflow:hidden}
.sig-prices{position:absolute;left:614px;top:30px}
.price-row{display:flex;align-items:center;gap:6px;height:23px;white-space:nowrap}
.price-row b{font-family:'Oswald',sans-serif;font-size:19px;color:var(--ink);font-weight:600;width:58px;text-align:right}
.price-row span{font-family:'Oswald',sans-serif;font-size:8.5px;line-height:.95;text-transform:uppercase;color:var(--ink)}
.classic-stack{font-family:'Alfa Slab One',serif;font-size:23px;line-height:.98;color:var(--sauce)}
.cp .n{font-family:'Oswald',sans-serif;font-weight:600;font-size:15px;letter-spacing:1px;line-height:1}
.cp .d{font-size:7px;text-transform:uppercase;color:var(--sepia);margin-bottom:5px}
.hand{font-family:'Oswald',sans-serif;font-size:8.5px;text-transform:uppercase}
</style>
</head>
<body>
<div class="menu">
  <div class="rule-v"></div>

  <div class="art" role="img" aria-label="Sketched basket of fries" style="left:205px;top:120px;width:195px;height:170px;background:radial-gradient(ellipse,#a68b6c 0%,rgba(204,176,139,0) 70%)"></div>
  <div class="art" role="img" aria-label="Sketched round Italian bread loaves" style="left:330px;top:930px;width:160px;height:100px;background:radial-gradient(ellipse,#a68b6c 0%,rgba(204,176,139,0) 70%)"></div>
  <div class="art" role="img" aria-label="Sketched sliced pizza" style="left:640px;top:615px;width:160px;height:180px;border-radius:50%;background:radial-gradient(circle,#a88e70 0%,rgba(204,176,139,0) 70%)"></div>

  <h1 class="slab abs" style="left:28px;top:20px;font-size:32px">STARTERS</h1>
  <div class="col" style="left:28px;top:74px;width:165px">
    <div class="item">Wings <span class="p">$9</span></div>
    <div class="desc">10 jumbo wings shaken in our homemade zesty wing sauce [mild, hot, bbq, garlic parm or sweet &amp; sour]<br>additional side sauces -0.50</div>
    <div class="item">Cheesy Herb<br>Bread Sticks <span class="p">$4</span></div>
    <div class="desc">Savory cheese &amp; herb blend melted until soft &amp; gooey in the center of our bread sticks, topped with sesame seeds, served with a side of sauce</div>
    <div class="item">Garlic Knots <span class="p">$3.50</span></div>
    <div class="desc">Served with a side of sauce</div>
    <div class="item">Buffalo Knots <span class="p">$5</span></div>
    <div class="desc">Served with a side of bleu cheese</div>
    <div class="item">1 lb of Fries <span class="p">$5</span></div>
    <div class="desc">Served with a side of sauce [plain, sesame or garlic]</div>
  </div>
  <div class="col" style="left:209px;top:74px;width:170px">
    <div class="item">Killer Bread Sticks <span class="p">$3</span></div>
    <div class="desc">Served with a side of sauce [plain, sesame or garlic]</div>
    <div class="item">Mozzarella Sticks <span class="p">$6</span></div>
    <div class="desc">Served with a side of sauce</div>
    <div class="item">Boneless Wings <span class="p">$6.50</span></div>
    <div class="desc">Shaken in our homemade zesty wing sauce mild, hot, bbq, garlic parm or sweet &amp; sour<br>additional side sauces -0.50</div>
    <div class="item">Tenders <span class="p">$6.50</span></div>
    <div class="desc">Served with choice of sauce on the side buffalo, bbq, garlic parm, marinara or sweet &amp; sour</div>
  </div>

  <h2 class="script abs" style="left:148px;top:258px;font-size:36px">Salads</h2>
  <div class="col" style="left:28px;top:326px;width:170px">
    <div class="sal">Antipasto <span class="p">$9</span></div>
    <div class="desc">Salami, hot ham, pepperoni, roasted red peppers, hot peppers, tomatoes, olives, parmesan &amp; provolone cheese</div>
    <div class="sal">Chicken Salad <span class="p">$9</span></div>
    <div class="item" style="font-size:10px">Grilled, crispy<br>or buffalo chicken</div>
    <div class="desc">Romaine, parmesan, tomatoes, onions &amp; choice of dressing</div>
    <div class="sal">Cranberry Walnut<br>Chicken Salad <span class="p">$9</span></div>
    <div class="desc">Grilled chicken, walnuts, dried cranberries &amp; parmesan over a bed of romaine-spinach blend, served with our vinaigrette dressing</div>
    <div class="sal">Caesar Salad <span class="p">$8</span></div>
    <div class="desc">Romaine, parmesan, croutons &amp; caesar dressing<br>&nbsp;&nbsp;&nbsp;with chicken - $9</div>
  </div>
  <div class="col" style="left:209px;top:326px;width:170px">
    <div class="sal">Garden Salad <span class="p">$4</span></div>
    <div class="desc">Romaine, tomatoes, onion, cucumber &amp; choice of dressing<br>&nbsp;&nbsp;&nbsp;family - $6<br>&nbsp;&nbsp;&nbsp;add turkey or ham - $1.50</div>
    <div class="sal" style="font-size:12.5px">☞ Dressing Choices:</div>
    <div class="desc" style="padding-left:28px;line-height:1.5">Parmesan peppercorn<br>Honey mustard<br>Ranch<br>Caesar<br>Bleu cheese<br>Russian<br>Italian<br>House vinaigrette<br>Balsamic vinaigrette<br>&nbsp;&nbsp;&nbsp;additional dressing - $0.75</div>
  </div>

  <h2 class="slab abs" style="left:0;width:399px;text-align:center;top:546px;font-size:30px">WRAPS</h2>
  <div class="sub abs" style="left:0;width:399px;top:588px">On plain or whole wheat wrap <span style="color:var(--ink)">$8</span></div>
  <div class="col" style="left:28px;top:612px;width:170px">
    <div class="item">Buffalo</div>
    <div class="desc">Crispy chicken shaken in wing sauce, lettuce &amp; tomatoes with bleu cheese dressing</div>
    <div class="item">Chipotle Turkey</div>
    <div class="desc">Turkey, romain, roasted red peppers, tomatoes &amp; chipotle mayo</div>
    <div class="item">Saratoga Veggie</div>
    <div class="desc">Eggplant, romaine, arugula, roasted red peppers, tomatoes, onions &amp; parmesan cheese with balsamic vinaigrette dressing</div>
    <div class="item">Caesar</div>
    <div class="desc">Romaine, grilled chicken &amp; parmesan cheese with caesar dressing</div>
  </div>
  <div class="col" style="left:210px;top:612px;width:175px">
    <div class="item">Grilled<br>Chicken Basil</div>
    <div class="desc">Grilled chicken, pesto mayo, tomatoes, onions &amp; fresh mozzarella</div>
    <div class="item">Create Your Own</div>
    <div class="desc">Charges apply for additional ingredients</div>
    <div class="desc" style="display:grid;grid-template-columns:1fr 1fr;gap:0 6px;margin-bottom:2px"><span>Choose one:<br>&nbsp;&nbsp;&nbsp;Turkey<br>&nbsp;&nbsp;&nbsp;Ham<br>&nbsp;&nbsp;&nbsp;Grilled chicken</span><span><br>Crispy chicken<br>Eggplant<br>Roast beef</span></div>
    <div class="desc" style="display:grid;grid-template-columns:1fr 1fr;gap:0 6px"><span>Pick four fixens:<br>&nbsp;&nbsp;&nbsp;Lettuce<br>&nbsp;&nbsp;&nbsp;Roasted red peppers<br>&nbsp;&nbsp;&nbsp;Black olives<br>&nbsp;&nbsp;&nbsp;Green peppers</span><span><br>Tomatoes<br>Pickles<br>Onions<br>Hot peppers</span></div>
  </div>

  <h2 class="abs" style="left:0;width:399px;text-align:center;top:794px;font-family:'Bebas Neue',sans-serif;font-size:46px;color:var(--sauce);letter-spacing:1px;line-height:1">MOONS</h2>
  <div class="abs" style="left:0;width:399px;top:848px;text-align:center;font-family:'Bebas Neue',sans-serif;font-size:11px;color:var(--sauce)">Our version of a sub, on our baked-in-store Italian bread rounds</div>
  <div class="col" style="left:28px;top:872px;width:180px">
    <div class="item">Italian Mixed <span class="p">$8</span></div>
    <div class="desc" style="margin-bottom:2px">Salami, hot ham &amp; pepperoni</div>
    <div class="item">Veggie <span class="p">$8</span></div>
    <div class="desc" style="margin-bottom:2px">Eggplant, roasted red peppers, spinach, arugula, tomatoes &amp; onions</div>
    <div class="item" style="line-height:1.25">Turkey <span class="p">$8</span><br>Ham <span class="p">$8</span><br>Roast Beef <span class="p">$8</span></div>
  </div>
  <div class="col" style="left:211px;top:872px;width:180px">
    <div class="item" style="line-height:1.2">Turkey<br>and Bacon <span class="p">$9</span><br>BLT <span class="p">$9</span><br>Meatball Parm <span class="p">$9</span><br>Chicken Parm <span class="p">$9</span><br>Eggplant Parm <span class="p">$9</span></div>
  </div>
  <div class="abs" style="left:28px;top:990px;width:50px;height:52px;border:1px solid var(--sauce);font-family:'Bebas Neue',sans-serif;font-size:8px;line-height:1.05;color:var(--sauce);text-align:center;padding-top:5px">Includes<br>four fixens<br>and one<br>cheese</div>
  <div class="desc abs" style="left:82px;top:994px;width:310px;line-height:1.55">Fixens: lettuce, tomatoes, onions, green peppers, roasted red peppers, black olives, pickles and hot peppers<br>Cheese: American, provolone, swiss and mozzarella<br>Charges apply for traditional ingredients</div>

  <div class="abs" style="left:24px;top:1064px;width:180px;font-family:'Rye',serif;color:var(--sauce);line-height:1;white-space:nowrap">
    <div style="font-size:30px;padding-left:22px">Calzones</div>
    <div style="font-size:9px;padding-left:6px;margin-top:-4px">AND</div>
    <div style="font-size:30px">Strombolis</div>
  </div>
  <div class="col" style="left:212px;top:1066px;width:180px">
    <div class="item">Calzone <span class="p">$8</span></div>
    <div class="desc">Stuffed bread with ricotta, mozzarella &amp; romano cheese<br>additional toppings: add $1 [each]</div>
    <div class="item">Stromboli <span class="p">$8</span></div>
    <div class="desc">Stuffed bread with mozzarella &amp; romano<br>additional toppings: add $1 [each]</div>
  </div>

  <!-- SIGNATURE PIZZA -->
  <div class="sig-title">
    <div class="script" style="font-size:36px;line-height:1;padding-left:30px">Signature</div>
    <div style="font-family:'Rye',serif;font-size:44px;color:var(--sauce);line-height:.95;margin-top:-6px">PIZZA</div>
    <div style="font-family:'Bebas Neue',sans-serif;font-size:12px;margin-top:6px;color:var(--ink)">NY Style • Thin Crust • Round Pizza</div>
  </div>
  <div class="sig-prices">
    <div class="price-row"><b>9.25</b><span>Personal<br>10" - 6 cut</span></div>
    <div class="price-row"><b>16.25</b><span>Medium<br>14" - 8 cut</span></div>
    <div class="price-row"><b>19.25</b><span>Family<br>18" - 12 cut</span></div>
    <div class="price-row"><b>9.25</b><span>Gluten-free<br>small</span></div>
    <div class="price-row"><b>16.25</b><span>Gluten-free<br>medium</span></div>
  </div>

  <div class="pz" style="left:405px;top:162px"><div class="n" style="font-family:'Special Elite',cursive;font-size:19px">Buffalo Pie</div><div class="d">Seasoned diced chicken with our famous homemade wing sauce &amp; bleu cheese, loaded with mozzarella</div></div>
  <div class="pz" style="left:405px;top:216px"><div class="n" style="font-family:'Playfair Display',serif;font-size:19px">Tree Hugger</div><div class="d">Spinach, tomatoes, mushrooms &amp; broccoli</div></div>
  <div class="pz" style="left:405px;top:272px"><div class="n" style="font-family:'Oswald',sans-serif;font-weight:600;font-size:19px;letter-spacing:1px">PIE-CASSO</div><div class="d">White pizza with broccoli, tomatoes &amp; ricotta</div></div>
  <div class="pz" style="left:405px;top:322px"><div class="n" style="font-family:'Bebas Neue',sans-serif;font-size:24px">-CARCASS-</div><div class="d">Sausage, pepperoni bacon &amp; meatballs</div></div>
  <div class="pz" style="left:405px;top:366px"><div class="n" style="font-family:'Yellowtail',cursive;font-size:24px">Chicken</div><div class="n" style="font-family:'Oswald',sans-serif;font-size:9px;letter-spacing:3px">C·A·E·S·A·R</div><div class="d">Caesar sauce &amp; grilled chicken, topped with crisp romaine</div></div>
  <div class="pz" style="left:405px;top:434px"><div class="n" style="font-family:'Yellowtail',cursive;font-size:24px">Chicken</div><div class="n" style="font-family:'Oswald',sans-serif;font-size:14px">BACON RANCH</div><div class="d">Chicken &amp; bacon over buttermilk ranch sauce.<br>Veggie style: spinach, mushrooms &amp; tomatoes</div></div>
  <div class="pz" style="left:405px;top:516px"><div class="n" style="font-family:'Alfa Slab One',serif;font-size:18px;color:var(--sepia)">GARDEN<br>OF EDEN</div><div class="d">Honey mustard sauce, spinach, tomatoes &amp; mushrooms. Kick it up with hot peppers and chicken - add $3</div></div>

  <div class="pz" style="left:592px;top:166px"><div class="n" style="font-family:'Special Elite',cursive;font-size:16px">BREADSTICK PIE</div><div class="d">Garlic butter, mozzarella cheese &amp; dollops of marina</div></div>
  <div class="pz" style="left:592px;top:210px"><div class="n" style="font-family:'Alfa Slab One',serif;font-size:19px">BBQ</div><div class="d">White pizza with broccoli, tomatoes &amp; ricotta</div></div>
  <div class="pz" style="left:592px;top:256px"><div class="n" style="font-family:'Yellowtail',cursive;font-size:24px">Chicken</div><div class="n" style="font-family:'Special Elite',cursive;font-size:13px">BASIL PESTO</div><div class="d">Fresh basil pesto sauce, chicken &amp; tomatoes</div></div>
  <div class="pz" style="left:592px;top:320px"><div class="n" style="font-family:'Yellowtail',cursive;font-size:24px">Chicken</div><div class="n" style="font-family:'Oswald',sans-serif;font-size:12px;letter-spacing:1px">PARM</div><div class="d">Crispy breaded chicken over marinara sauce, ricotta dollops &amp; smothered in mozzarella</div></div>
  <div class="pz" style="left:592px;top:398px"><div class="n" style="font-family:'Oswald',sans-serif;font-weight:600;font-size:14px;letter-spacing:1px">SOUTH OF<br>THE BORDER</div><div class="d">Pizza smothered with cheese, seasoned taco beef, salsa, fresh tomatoes and sour cream, topped with romaine lettuce</div></div>
  <div class="pz" style="left:592px;top:462px"><div class="n" style="font-family:'Oswald',sans-serif;font-weight:500;font-size:12px;letter-spacing:1px">ROAST BEEF PEPPERCORN</div><div class="d" style="margin-top:1px">The Holloway</div><div class="d">In-store roasted beef atop our creamy peppercorn sauce and smothered with mozzarella cheese</div></div>
  <div class="pz" style="left:592px;top:520px"><div class="n" style="font-family:'Yellowtail',cursive;font-size:17px;line-height:.95">Arugula <span style="font-size:10px">and</span><br>Proscuitto</div><div class="d">White pizza with thinly sliced prosciutto, mozzarella &amp; parmesan finished with arugula &amp; balsamic glaze</div></div>

  <div class="rule-h" style="top:601px"></div>

  <div class="classic-stack abs" style="left:412px;top:616px">
    <div>CLASSIC</div><div>PIZZA</div>
    <div style="opacity:.8">CLASSIC</div><div style="opacity:.8">PIZZA</div>
    <div style="opacity:.55">CLASSIC</div><div style="opacity:.55">PIZZA</div>
    <div style="opacity:.3">CLASSIC</div><div style="opacity:.3">PIZZA</div>
  </div>
  <div class="abs" style="left:522px;top:612px;width:1px;height:186px;background:var(--rule);opacity:.6"></div>
  <div class="cp abs" style="left:532px;top:622px;width:255px">
    <div class="n">SPO</div><div class="d">Personal $9.25 // medium $15.75 // family $19.25<br>sausage, peppers &amp; onions</div>
    <div class="n">TOMATO PIE</div><div class="d">Personal $7.25 // medium $12.75 // family $15.25</div>
    <div class="n">WHITE GARLIC</div><div class="d">Personal $7.25 // medium $12.75 // family $15.25</div>
    <div class="n">MARGHERITA</div><div class="d">Personal $8.25 // medium $14.75 // family $17.25<br>classic marinara sauce, fresh mozzarella &amp; basil</div>
    <div class="n">OLD SCHOOL EBA</div><div class="d">Personal $10.25 // medium $17.75 // family $20.25<br>everything but anchovies: sausage, mushrooms, peppers &amp; pepperoni. A favorite when we had only five toppings!</div>
  </div>

  <div class="rule-h" style="top:827px"></div>

  <div class="abs" style="left:414px;top:862px;width:110px;text-align:center;font-family:'Bebas Neue',sans-serif;font-size:31px;line-height:.92;color:var(--sauce)">CREATE<br>YOUR<br>OWN</div>
  <div class="abs" style="left:530px;top:840px;width:256px">
    <div class="hand">☞ Start with the cheese:</div>
    <div class="desc" style="font-size:7px;margin-bottom:4px">Personal $6.75 // medium $11.75 // family $13.25<br>gluten-free: small $6.25 // medium $11.25</div>
    <div class="hand">☞ Add toppings:</div>
    <div class="desc" style="font-size:7px;margin-bottom:4px">Personal $1 // medium $1.50 // family $2</div>
    <div class="hand">☞ Topping choices:</div>
    <div class="desc" style="font-size:7px;font-weight:700">Pepperoni, sausage, eggplant, grilled chicken, crispy chicken, ham, salami, roast beef, bacon, meatballs, mushrooms, green peppers, broccoli, tomatoes, roasted red peppers, black olives, onions, spinach, banana peppers, pineapple &amp; anchovies.</div>
  </div>

  <div class="rule-h" style="top:996px"></div>

  <div class="abs" style="left:416px;top:1010px;font-family:'Yellowtail',cursive;color:var(--sauce);line-height:1;white-space:nowrap">
    <div style="font-size:44px">Pasta</div>
    <div style="font-size:18px;padding-left:96px;margin-top:-10px">and more</div>
  </div>
  <div class="col" style="left:422px;top:1082px;width:170px">
    <div class="item" style="font-size:11.5px">Pasta Marinara <span class="p">$7</span></div>
    <div class="desc">A generous portion of penne or linguine, with classic marinara sauce<br>with meatballs -$3</div>
    <div class="item" style="font-size:11.5px">Eggplant<br>Parmesan <span class="p">$9</span></div>
    <div class="desc">Breaded eggplant with marinara sauce and melted mozzarella served over a bread of pasta</div>
  </div>
  <div class="col" style="left:611px;top:1010px;width:172px">
    <div class="item" style="font-size:11.5px">Lasagna <span class="p">$10</span></div>
    <div class="desc">Homemade with ricotta, slices of sausage &amp; meatballs layered with blended cheeses</div>
    <div class="item" style="font-size:11.5px">Tortellini<br>Alfredo <span class="p">$9</span></div>
    <div class="desc">Cheese filled tortellini over classic alfredo sauce and melted mozzarella served over a bread of pasta<br>also available with marinara sauce</div>
    <div class="item" style="font-size:11.5px">Chicken<br>Parmesan <span class="p">$</span></div>
    <div class="desc">Breaded chicken with marinara sauce and melted mozzarella served over a bed of pasta</div>
  </div>
</div>
</body>
</html>
```